Metal Fabrication Business Cards

We need a business card for our business of Metal Fabrication/Welding. Our company is called "Hadley's Metal Fabrication"

We are a metal fabrication business which takes on "high class" clients- dealing with some of the biggest builders in Australia. Our work is neat, and the type of work we do is 2nd to none for quality. We want to show that on our cards. However, we would love to show a side that is down to earth and a bit more modern and contemporary - we are all young in business so would love to show that side - rather than a boring "very straight looking" card. We always have a clean workshop and take pride in our presentation. We want to come across like we are very rich, but would love to go for a surf as well! A card that basically says we have high class and will charge you a high rate - but the quality will be outstanding.

Front of card: - Simply but sharp!
-Thinking maybe white card - with nice black writing.
-On the right hand side of card a person welding - or holding a welder.
- My business name - Hadley's Metal Fabrication
-Also maybe my name - which is 'Corey" (if it doesn't work, we can put this on the back of card.)
- if needed to look better - we can put keywords on front of card like "metal fabrication, sheet metal, welding etc" but I dont want it to be crowded.

Back of card: - Also make smart but sharp!
Put details such as:
04376 81 302
hadley.fabrication@mailbox-ink.com
7/23 Heron Street
East Kelsey NSW 2519
www.ridgewayfabrication.com.au
ABN 71 530 864 217

thats just an idea - its now up to you. I don't mind what you come up with - as long as it stands out from the rest and looks sharp, professional but contemporary.

Business

Put details such as:
04376 81 302
7/23 Heron Street
East Kelsey NSW 2519
ABN 71 530 864 217

Hadley's Metal Fabrication

```html
<!DOCTYPE html>
<html lang="en">
<head>
<meta charset="utf-8">
<title>Hadley's Metal Fabrication – Business Card</title>
<link rel="stylesheet" href="https://fonts.googleapis.com/css2?family=Courgette&family=Tinos:wght@400;700&display=swap">
<style>
  :root {
    --bg: #cbcbcb;
    --card: #ffffff;
    --brand-blue: #3a53a8;
    --band-blue: #3d55aa;
    --ink: #111111;
    --swoosh: #161616;
    --on-band: #f2f4fb;
  }
  * { margin: 0; padding: 0; box-sizing: border-box; }
  html, body {
    width: 1189px;
    height: 1200px;
    overflow: hidden;
    background: var(--bg);
  }
  .canvas {
    position: relative;
    width: 1189px;
    height: 1200px;
  }
  .card {
    position: absolute;
    left: 194px;
    width: 808px;
    height: 461px;
    background: var(--card);
    overflow: hidden;
  }
  .card--front { top: 110px; }
  .card--back { top: 620px; }

  .brand-name {
    font-family: "Courgette", "Georgia", cursive;
    font-weight: 400;
    color: var(--brand-blue);
    white-space: nowrap;
    position: absolute;
    line-height: 1.2;
  }
  .card--front .brand-name {
    left: 56px;
    top: 42px;
    font-size: 42px;
  }
  .card--back .brand-name {
    left: 0;
    right: 0;
    text-align: center;
    top: 114px;
    font-size: 42px;
  }

  .contact-list {
    position: absolute;
    left: 56px;
    top: 224px;
    list-style: none;
    font-family: "Tinos", "Times New Roman", serif;
    font-size: 24px;
    color: var(--ink);
    line-height: 26px;
  }
  .contact-list li {
    display: flex;
    align-items: center;
    gap: 13px;
  }
  .contact-icon {
    width: 17px;
    height: 17px;
    flex: none;
  }

  .holder-name {
    position: absolute;
    right: 54px;
    top: 236px;
    font-family: "Tinos", "Times New Roman", serif;
    font-weight: 700;
    font-size: 36px;
    color: var(--ink);
  }

  .wave {
    position: absolute;
    left: 0;
    top: 0;
    width: 808px;
    height: 461px;
  }
  .address {
    position: absolute;
    left: 56px;
    top: 392px;
    font-family: "Tinos", "Times New Roman", serif;
    font-size: 24px;
    color: var(--on-band);
    white-space: nowrap;
  }

  .services {
    position: absolute;
    left: 0;
    right: 0;
    top: 308px;
    text-align: center;
    font-family: "Tinos", "Times New Roman", serif;
    font-size: 28px;
    color: var(--ink);
  }
</style>
</head>
<body>
<main class="canvas">

  <section class="card card--front" aria-label="Card front">
    <svg class="wave" viewBox="0 0 808 461" aria-hidden="true">
      <path fill="var(--swoosh)" d="M0,372 C120,328 300,346 470,358 C620,368 740,356 808,290 L808,382 C700,392 560,384 470,374 C300,358 130,350 0,372 Z"/>
      <path fill="var(--band-blue)" d="M0,376 C140,354 300,364 470,380 C620,394 730,402 808,394 L808,461 L0,461 Z"/>
    </svg>

    <h1 class="brand-name">Hadley's Metal Fabrication</h1>

    <ul class="contact-list">
      <li>
        <svg class="contact-icon" viewBox="0 0 17 17" aria-hidden="true">
          <rect width="17" height="17" fill="var(--brand-blue)"/>
          <path fill="#fff" d="M5,3 L7,3 L8,6 L6.6,7.2 C7.3,8.8 8.3,9.8 9.8,10.5 L11,9 L14,10 L14,12.2 C14,13 13.3,13.6 12.5,13.5 C7.8,13 4,9.2 3.5,4.5 C3.4,3.7 4.1,3 5,3 Z"/>
        </svg>
        <span>04376 81 302</span>
      </li>
      <li>
        <svg class="contact-icon" viewBox="0 0 17 17" aria-hidden="true">
          <rect width="17" height="17" fill="var(--brand-blue)"/>
          <rect x="3" y="5" width="11" height="8" fill="none" stroke="#fff" stroke-width="1.3"/>
          <path d="M3,5 L8.5,9.5 L14,5" fill="none" stroke="#fff" stroke-width="1.3"/>
        </svg>
        <span>hadley.fabrication@mailbox-ink.com</span>
      </li>
      <li>
        <svg class="contact-icon" viewBox="0 0 17 17" aria-hidden="true">
          <rect width="17" height="17" fill="var(--brand-blue)"/>
          <circle cx="8.5" cy="8.5" r="5.2" fill="none" stroke="#fff" stroke-width="1.3"/>
          <ellipse cx="8.5" cy="8.5" rx="2.2" ry="5.2" fill="none" stroke="#fff" stroke-width="1"/>
          <line x1="3.3" y1="8.5" x2="13.7" y2="8.5" stroke="#fff" stroke-width="1"/>
        </svg>
        <span>www.ridgewayfabrication.com.au</span>
      </li>
    </ul>

    <p class="holder-name">Corey</p>

    <p class="address">7/23 Heron Street East Kelsey NSW 2519</p>
  </section>

  <section class="card card--back" aria-label="Card back">
    <h2 class="brand-name">Hadley's Metal Fabrication</h2>
    <p class="services">"metal fabrication, sheet metal, welding etc"</p>
  </section>

</main>
</body>
</html>
```